Need Bus charter business website,

I am starting a bus charter business in the near future. I am based in Geelong, Victoria in Australia. I will have a 25 or 28 seater bus that will be used to take people on charted trips. Whether they be to birthday parties, weddings, sporting events, corporate events, mystery trips, going down the Great Ocean Road, or anywhere someone wants. As for colour scheme, I'm leaning towards something blue and grey, but open to anything really that catches my eye. I played around with a basic web design program and made a basic site which I uploaded ( www.kelmoride.com.au) It has things which I wanted to include such as, services I will provide, trip information, contact form etc.

I don't mind if the layout is completely different to my site as it was only a template that was included in the program I used. I would like the overall design to be relatively fluid, not having to back-track a lot to navigate the site.

```html
<!DOCTYPE html>
<html lang="en">
<head>
<meta charset="utf-8">
<title>Kelmo Ride Tours</title>
<link href="https://fonts.googleapis.com/css2?family=Roboto+Condensed:wght@300;400;700&family=Arimo:wght@400;700&display=swap" rel="stylesheet">
<style>
:root{
  --blue:#0a6fc4;
  --blue-dark:#0b55a0;
  --teal:#1f5666;
  --olive:#8a8558;
  --orange:#e06a12;
  --ink:#222;
  --beige:#ece9dc;
  --line:#cfc9aa;
}
*{box-sizing:border-box;margin:0;padding:0}
html,body{width:1200px;height:1200px;overflow:hidden}
body{position:relative;background:linear-gradient(#fff 560px,#f1f0ec 700px,#f7f7f5 1090px);font-family:"Arimo",sans-serif;color:var(--ink)}
.abs{position:absolute}
.hero{left:0;top:0;width:1200px;height:564px;background:linear-gradient(180deg,#7fb0de 0%,#c7dcef 20%,#e8eef2 32%,#7d8a96 55%,#4a4f55 85%,#6c6f72 100%)}
.topbar{left:66px;top:0;width:1070px;height:40px;background:#fff;font-size:17px}
.topbar span{position:absolute;top:11px;white-space:nowrap}
.lang{left:934px;top:0;width:136px;height:40px;background:linear-gradient(#f6f4ea,#e3dfcc);border-left:1px solid #d9d4bc}
.lang b{position:absolute;left:14px;top:11px;font-weight:400;font-size:17px}
.lang i{position:absolute;right:0;top:0;width:34px;height:40px;border-left:1px solid #cfc9aa}
.lang i:after{content:"";position:absolute;left:9px;top:14px;border:8px solid transparent;border-top:10px solid var(--olive)}
.navbar{left:66px;top:40px;width:1070px;height:60px;background:linear-gradient(#fbfaf3,#e8e4d1);box-shadow:0 3px 5px rgba(0,0,0,.3)}
.brand{left:12px;top:14px;display:flex;align-items:center;gap:10px;font-family:"Arimo",sans-serif;font-weight:700;font-size:27px;color:#111;white-space:nowrap}
.brand i{width:22px;height:22px;background:#111}
.menu{left:366px;top:19px;width:690px;display:flex;justify-content:space-between;font-size:17px;white-space:nowrap}
.menu a{color:#222;text-decoration:none}
.menu a:before{content:"▶";font-size:12px;margin-right:5px;vertical-align:2px}
.finder{left:66px;top:120px;width:264px;height:168px;background:var(--blue);color:#fff}
.finder p{position:absolute;left:14px;top:10px;font-size:17px}
.select{position:absolute;left:10px;top:40px;width:244px;height:38px;background:#fff;border:1px solid #ccc;color:#333;font-size:17px;padding:8px 6px}
.select i{position:absolute;right:0;top:0;width:34px;height:36px;background:#f0ede2;border-left:1px solid #ccc}
.select i:after{content:"";position:absolute;left:9px;top:12px;border:8px solid transparent;border-top:10px solid var(--olive)}
.book{position:absolute;left:14px;top:99px;width:236px;height:36px;background:linear-gradient(#4b8ee0,#1a58b0);border:1px solid #0c3d7c;text-align:center;color:#0a2550;font-weight:700;font-size:19px;line-height:34px}
.finder small{position:absolute;left:0;width:100%;top:150px;text-align:center;font-size:12px;font-weight:700}
.arrow{top:230px}
.dots{top:452px;left:970px;display:flex;gap:14px}
.dots i{width:22px;height:22px;border-radius:50%;background:#222}
.dots i.on{background:#1ba5e6}
.cats{left:68px;top:486px;width:1067px;height:132px;display:flex;box-shadow:0 2px 6px rgba(0,0,0,.3)}
.cat-img{height:100%}
.cat-text{height:100%;color:#fff;padding:30px 16px 0;font-family:"Roboto Condensed",sans-serif}
.cat-text h3{font-weight:400;font-size:28px;white-space:nowrap}
.cat-text p{font-size:17px;font-weight:300;line-height:20px}
.welcome-img{left:72px;top:666px;width:288px;height:168px;border-radius:10px;background:radial-gradient(ellipse at center,#f4f4f4,#d9dde2 70%,rgba(255,255,255,0) 72%)}
.sec h2{font-family:"Roboto Condensed",sans-serif;font-weight:400;color:var(--olive);font-size:29px;line-height:34px;white-space:nowrap}
.sec p{font-family:"Roboto Condensed",sans-serif;font-size:16px;line-height:20px;color:#222}
.more{color:var(--orange);font-size:19px}
.vline{width:1px;background:var(--line)}
.hline{height:1px;background:#c8c2a0}
.interior{left:816px;top:654px;width:354px;height:240px;background:linear-gradient(180deg,#e3e6ee,#b5bccb 50%,#8f98aa);box-shadow:0 0 18px 12px #fff inset}
.footer{left:0;top:1098px;width:1200px;height:102px;background:linear-gradient(#d0cfcb,#f6f6f4 18px,#fff)}
.flinks{left:22px;top:1134px;font-size:17px;color:#333;white-space:nowrap}
.flinks span{margin:0 14px;color:#444}
.copy{left:34px;top:1168px;font-size:15px;text-decoration:underline;color:#333}
.social{display:flex;align-items:center;justify-content:center;font-size:15px;font-weight:700}
.fb{left:894px;top:1122px;width:144px;height:58px;background:#eef1f7;border:2px solid #3b5b98;color:#3b5b98}
.tw{left:1072px;top:1122px;width:90px;height:52px;background:#222;color:#fff;font-size:14px}
</style>
</head>
<body>
<div class="abs hero" role="img" aria-label="Photo of a tour group standing in front of a large white charter coach under a blue sky"></div>

<header>
  <div class="abs topbar">
    <span style="left:26px">My Tours</span>
    <span style="left:360px">Sign in !</span>
    <span style="left:472px">Not a member <span style="position:static;color:#444">Signup</span></span>
    <div class="abs lang"><b>language</b><i></i></div>
  </div>
  <nav class="abs navbar">
    <div class="abs brand"><i></i>Kelmo Ride Tours</div>
    <div class="abs menu"><a>Home</a><a>About us</a><a>Services</a><a>Trips&nbsp; on offer</a><a>Book a trip</a><a>Contact Us</a></div>
  </nav>
</header>

<div class="abs finder">
  <p>Where Would you want to go?</p>
  <div class="select">--Choose a Destination---<i></i></div>
  <div class="book">Book a Tour</div>
  <small>OFFERING BEST RATES?</small>
</div>

<svg class="abs arrow" style="left:14px" width="40" height="64"><path d="M34 4L6 32L34 60" fill="none" stroke="#fff" stroke-width="5"/></svg>
<svg class="abs arrow" style="left:1134px" width="40" height="64"><path d="M6 4L34 32L6 60" fill="none" stroke="#fff" stroke-width="5"/></svg>
<div class="abs dots"><i></i><i></i><i class="on"></i><i></i></div>

<section class="abs cats">
  <div class="cat-img" style="width:192px;background:linear-gradient(#bcd8ef,#e9e4d8 55%,#d8cbb0)" role="img" aria-label="Wedding arch decorated with white flowers on a beach"></div>
  <div class="cat-text" style="width:157px;background:var(--teal)"><h3>Weddings</h3><p>A small description comes here</p></div>
  <div class="cat-img" style="width:213px;background:linear-gradient(#7a9a5a,#4d6d35 55%,#8a5a30)" role="img" aria-label="Bottle of red wine and a glass in front of vineyard hills"></div>
  <div class="cat-text" style="width:175px;background:var(--blue)"><h3>Buck’s Party</h3><p>A small description comes here</p></div>
  <div class="cat-img" style="width:152px;background:linear-gradient(120deg,#e9ebe4,#fafaf7 50%,#c9d1c0)" role="img" aria-label="Bride holding a white bouquet"></div>
  <div class="cat-text" style="width:178px;background:var(--teal)"><h3>Hen’s Party</h3><p>A small description comes here</p></div>
</section>

<main>
  <div class="abs welcome-img" role="img" aria-label="White minibus side view"></div>
  <div class="abs sec" style="left:386px;top:678px;width:360px">
    <h2>Welcome to Kelmo Ride Tours:</h2>
    <p>We are an accredited bus company that operates bus trip and charter work in the Geelong area. We offer a range of <u>services</u>, from day trips down the Great ...</p>
    <span class="more">Learn More</span>
  </div>
  <div class="abs hline" style="left:22px;top:866px;width:732px"></div>
  <div class="abs vline" style="left:800px;top:652px;height:242px"></div>
  <div class="abs interior" role="img" aria-label="Interior of a coach with rows of patterned seats"></div>

  <div class="abs sec" style="left:12px;top:926px;width:370px">
    <h2>Want to book a trip?</h2>
    <p>If you would like to book one of the trips we currently offer, please check out our <u>Current Trips</u> page and take note of the code for the trip you would like to take. Please let us know the code when contacting us... <span class="more">Learn More</span></p>
  </div>
  <div class="abs vline" style="left:390px;top:912px;height:150px"></div>
  <svg class="abs" style="left:412px;top:968px" width="84" height="56" viewBox="0 0 84 56" aria-hidden="true">
    <g fill="none" stroke="#a8a8a8" stroke-width="7" stroke-dasharray="5 4"><circle cx="24" cy="32" r="17"/><circle cx="62" cy="18" r="12"/></g>
    <g fill="none" stroke="#a8a8a8" stroke-width="4"><circle cx="24" cy="32" r="9"/><circle cx="62" cy="18" r="5"/></g>
  </svg>
  <div class="abs sec" style="left:512px;top:926px;width:268px">
    <h2>Our Services?</h2>
    <p>We have a wide range of services to offer. From wedding guest transfers, transport for corporate events, Buck’s and Hen’s nights to winery tours and ...</p>
    <span class="more">Learn More</span>
  </div>
  <div class="abs sec" style="left:820px;top:922px;width:370px">
    <h2>Trips on offer?</h2>
    <p>Here you’ll be able to find all the trips we currently have on offer. If you’d like to join us on one them, simply click the enquire now link and fill out the contact form...<span class="more">Learn More</span></p>
  </div>
</main>

<footer>
  <div class="abs footer"></div>
  <div class="abs flinks">Home<span>|</span>About us<span>|</span>Services<span>|</span>Trips&nbsp; on offer<span>|</span>Book a trip<span>|</span>Contact Us</div>
  <div class="abs copy">Copyright 2014 Kelmo Ride Tours Pty Ltd. ACN: 204 517 388</div>
  <div class="abs social fb">Friendbook</div>
  <div class="abs social tw">Chirper</div>
</footer>
</body>
</html>
```